Web Design Project

Due to client commitments, we don't have time in-house to complete this project...
We need a design refresh for our web company! It's time for us to move things along, so we're looking to SketchHarbor to get this done!
Our clients tend to be associations and government, with some element of business clients. We need a design that appeals to this sophisticated target market.
Our current web site can be found at www.trellisbridge.ca. We are looking for a more personable, contemporary look for the new site design. However, you can see our logo on this site, and some of the content.
The design you provide will be implemented in Quilla. The design winner will only need to provide the PSD or Fireworks PNG format. We anticipate creating the template coding in-house.
However, if you have experience creating Quilla templates, please let us know as we may ask you to bid separately to do that phase of the project.
We've provided you with wireframes of the home page and the inside page, along with Adobe Illustrator and PSD versions of our logo.
For the home page, we've indicated that we'd like to have a slider implemented into the design. For the purpose of design, we believe we'll use this slider: http://demo.glintmodulary.com/tasty-foldout-carousel.html.
The slider will contain inspiration photos related to each of the tabs. Ideally, we would like you to suggest the images for the slider. The dimension of the slider can be adjusted. We would like more space for the image with less for the text. The slider height should be sufficient to ensure the image "stimulates" the audience and sets the tone for the landing page.
The wireframe is provided to illustrate the placement of content and menu items. The exact dimensions of each component can be revised as you see fit.
Our clients tend to be associations, non-profit, government, and business clients. We need a design that appeals to this sophisticated target market.

```html
<!DOCTYPE html>
<html lang="en">
<head>
<meta charset="utf-8">
<title>TrellisBridge Communications – Home</title>
<link rel="stylesheet" href="https://fonts.googleapis.com/css2?family=PT+Sans:ital,wght@0,400;0,700;1,400&display=swap">
<style>
:root{
  --bar:#2c2c2c;
  --nav:#343434;
  --nav-line:#4a4a4a;
  --orange:#f7941d;
  --orange-dark:#e07a0c;
  --red:#c1272d;
  --text:#4a4a4a;
  --muted:#5c5c5c;
  --white:#ffffff;
  --panel:#4b4b4b;
  --tab:#6f6f6f;
  --box:#f0f0f0;
  --line:#d9d9d9;
}
*{margin:0;padding:0;box-sizing:border-box}
html,body{width:880px;height:1200px;overflow:hidden;background:var(--white)}
body{position:relative;font-family:"PT Sans",Arial,sans-serif;color:var(--text);font-size:10px}

/* top bar */
.topbar{position:absolute;left:0;top:0;width:880px;height:45px;background:var(--bar)}
.topbar span{position:absolute;top:14px;font-size:11.5px;color:var(--white);white-space:nowrap}
.topbar .accent{color:var(--orange)}

/* header */
.brand{position:absolute;left:48px;top:62px;display:flex;align-items:center;gap:10px}
.brand-dot{width:64px;height:64px;border-radius:50%;background:var(--red)}
.brand-name{font-size:25px;font-weight:700;color:#333;letter-spacing:.5px}
.quote-btn{position:absolute;left:729px;top:62px;width:102px;height:26px;border-radius:3px;
  background:linear-gradient(#fba53a,var(--orange-dark));color:#222;font-size:11.5px;
  display:flex;align-items:center;justify-content:center}
.social{position:absolute;top:97px;width:26px;height:26px;border-radius:50%}
.social.one{left:749px;background:#5ec3ea;box-shadow:0 0 0 2px #d5eef8}
.social.two{left:788px;background:#2e5aa8;box-shadow:0 0 0 2px #d0daf0}

/* main nav */
.mainnav{position:absolute;left:0;top:137px;width:880px;height:48px;background:linear-gradient(#3c3c3c,#2e2e2e)}
.mainnav a{position:absolute;top:0;height:48px;display:flex;align-items:center;justify-content:center;
  color:var(--white);font-size:11.5px;text-decoration:none;border-right:1px solid var(--nav-line);white-space:nowrap}
.mainnav a.current{background:linear-gradient(#f9a535,var(--orange-dark));border-right:none}

/* slider */
.slider-shadow{position:absolute;left:59px;top:452px;width:762px;height:60px;
  background:linear-gradient(rgba(0,0,0,.12),rgba(255,255,255,0))}
.slider{position:absolute;left:59px;top:202px;width:760px;height:250px;background:var(--panel);border:1px solid #333}
.slide-photo{position:absolute;left:4px;top:4px;width:527px;height:240px;
  background:linear-gradient(90deg,#d8d9db 0%,#6d7482 30%,#2f3440 50%,#8b8d92 72%,#dfe2e6 100%)}
.arrow{position:absolute;top:108px;width:34px;height:32px;background:rgba(50,50,50,.8);border-radius:2px}
.arrow svg{display:block;margin:8px auto}
.tab{position:absolute;left:535px;width:220px;height:21px;background:var(--tab);color:var(--orange);
  font-size:11px;padding:3px 12px}
.tab svg{position:absolute;right:10px;top:7px}
.vision-text{position:absolute;left:547px;top:33px;width:205px;color:var(--white);font-size:9.3px;line-height:14.4px;text-align:justify}
.view-more{position:absolute;left:700px;top:111px;color:var(--orange);font-size:9.5px}

/* services */
.service{position:absolute;top:504px;width:145px}
.service h3{font-size:13px;font-weight:400;color:var(--red);text-align:center;height:25px;white-space:nowrap}
.service .thumb{width:145px;height:94px;border:1px solid var(--line);background:#fff;padding:6px;box-shadow:0 6px 6px -4px rgba(0,0,0,.15)}
.service .thumb div{width:100%;height:100%}
.service p{margin:11px 0 0 4px;font-size:9.6px;line-height:14.5px;color:var(--muted);letter-spacing:-.1px}

/* blog */
.section-title{position:absolute;top:698px;font-size:13px;font-weight:400;color:var(--red)}
.post-icon{position:absolute;left:50px}
.post-meta{position:absolute;left:95px;font-size:9.6px;color:#333;white-space:nowrap}
.post-meta i{margin-right:16px}
.post-text{position:absolute;left:95px;width:400px;font-size:9.5px;line-height:14.5px;color:#333;letter-spacing:-.15px}
.dash{position:absolute;left:49px;width:446px;border-top:1px dashed #555}

/* featured */
.feat-thumb{position:absolute;left:498px;width:93px;height:67px;border:1px solid var(--line);padding:3px;background:#fff}
.feat-thumb div{width:100%;height:100%}
.feat-text{position:absolute;left:602px;width:221px;font-size:9.5px;line-height:14.5px;text-align:justify;color:#333;letter-spacing:-.15px}

/* link boxes */
.linkbox{position:absolute;top:985px;width:152px;height:137px;background:var(--box)}
.linkbox h4{position:absolute;top:-8px;left:50%;transform:translateX(-50%);white-space:nowrap;
  background:linear-gradient(#555,#333);color:var(--white);font-size:11px;font-weight:400;
  padding:2px 11px;border-radius:3px}
.linkbox ul{list-style:none;position:absolute;left:30px;top:27px}
.linkbox li{position:relative;padding-left:13px;height:23px;font-size:10px;color:#333}
.linkbox li::before{content:"";position:absolute;left:0;top:2px;border-left:6px solid #555;border-top:4px solid transparent;border-bottom:4px solid transparent}

/* footer */
.footer{position:absolute;left:0;top:1152px;width:880px;height:48px;background:var(--bar);
  display:flex;align-items:center;justify-content:center;color:var(--white);font-size:11.5px;gap:9px}
.footer .accent{color:var(--orange)}
</style>
</head>
<body>

<header>
  <div class="topbar">
    <span class="accent" style="left:59px">www.MapleVaultPolls.ca</span>
    <span style="left:262px">www.OttawaQuillaDesign.ca</span>
    <span style="left:463px">Contact us today</span>
    <span style="left:596px">613-555-0142</span>
    <span style="left:715px">sales@trellisbridge.ca</span>
  </div>

  <div class="brand">
    <div class="brand-dot"></div>
    <div class="brand-name">TrellisBridge</div>
  </div>
  <a class="quote-btn">Request a Quote</a>
  <span class="social one" aria-label="Social profile"></span>
  <span class="social two" aria-label="Social profile"></span>

  <nav class="mainnav">
    <a class="current" style="left:48px;width:78px">Home</a>
    <a style="left:126px;width:97px">Web Design</a>
    <a style="left:223px;width:101px">Mobile Apps</a>
    <a style="left:324px;width:124px">Custom Software</a>
    <a style="left:448px;width:143px">Accessible PDF/HTML</a>
    <a style="left:591px;width:146px">CMS: Quilla / Fernly</a>
    <a style="left:737px;width:86px;border-right:none">Contact us</a>
  </nav>
</header>

<main>
  <div class="slider-shadow"></div>
  <section class="slider">
    <div class="slide-photo" role="img" aria-label="Team of smiling business professionals standing in front of office windows"></div>
    <span class="arrow" style="left:10px"><svg width="10" height="16"><path d="M8 1 1 8l7 7" stroke="#fff" stroke-width="2" fill="none"/></svg></span>
    <span class="arrow" style="left:489px"><svg width="10" height="16"><path d="M2 1l7 7-7 7" stroke="#fff" stroke-width="2" fill="none"/></svg></span>

    <div class="tab" style="top:6px">Our Vision<svg width="10" height="6"><path d="M0 6 5 0l5 6z" fill="#fff"/></svg></div>
    <p class="vision-text">Corvinus are also reproduced in their exact original form, accompanied by English versions from the 1914 translation by H. Ashcombe &nbsp;The standard chunk of Lorem Ipsum used since the 1500s is reproduced below for those interested.</p>
    <span class="view-more">View more...</span>
    <div class="tab" style="top:136px">Business<svg width="10" height="6"><path d="M0 0l5 6 5-6z" fill="#fff"/></svg></div>
    <div class="tab" style="top:170px">Government<svg width="10" height="6"><path d="M0 0l5 6 5-6z" fill="#fff"/></svg></div>
    <div class="tab" style="top:204px">Associations / Non Profit<svg width="10" height="6"><path d="M0 0l5 6 5-6z" fill="#fff"/></svg></div>
  </section>

  <section class="services">
    <article class="service" style="left:51px"><h3>Web Design</h3><div class="thumb"><div role="img" aria-label="Figure painting a splash of blue" style="background:linear-gradient(135deg,#eef1f6,#4b7fd0 45%,#f2f2f2)"></div></div><p>Corvinus are also reproduced in their exact original form.</p></article>
    <article class="service" style="left:210px"><h3>Mobile Apps</h3><div class="thumb"><div role="img" aria-label="Smartphone surrounded by app icons" style="background:radial-gradient(circle,#333 20%,#8fb3d9 55%,#f4f4f4)"></div></div><p>Corvinus are also reproduced in their exact original form.</p></article>
    <article class="service" style="left:368px"><h3>Custom Software</h3><div class="thumb"><div role="img" aria-label="Stack of blue cubes" style="background:radial-gradient(circle,#7fa6c9 25%,#f5f7fa 70%)"></div></div><p>Corvinus are also reproduced in their exact original form.</p></article>
    <article class="service" style="left:527px"><h3>Accessible PDF / HTML</h3><div class="thumb"><div role="img" aria-label="Document file icons" style="background:linear-gradient(90deg,#f4f4f4,#c8c8c8 30%,#b32020 40%,#f0f0f0 60%,#e6eaf4)"></div></div><p>Corvinus are also reproduced in their exact original form.</p></article>
    <article class="service" style="left:685px"><h3>CMS: Quilla / Fernly</h3><div class="thumb"><div role="img" aria-label="Green globe connected to a computer mouse" style="background:radial-gradient(circle at 35% 50%,#6fb04a 22%,#d9e6d2 45%,#f6f6f6 70%)"></div></div><p>Corvinus are also reproduced in their exact original form.</p></article>
  </section>

  <section class="blog">
    <h2 class="section-title" style="left:49px">Blog</h2>
    <svg class="post-icon" style="top:732px" width="28" height="24" viewBox="0 0 28 24"><ellipse cx="11" cy="9" rx="11" ry="8" fill="#333"/><path d="M4 14l-2 6 7-4z" fill="#333"/><ellipse cx="19" cy="15" rx="9" ry="6.5" fill="#555"/><path d="M24 19l3 4-7-3z" fill="#555"/></svg>
    <p class="post-meta" style="top:738px"><i>Posted by : Martin</i> Posted on : <i>Dec 22, 2011 5.16 pm</i></p>
    <p class="post-text" style="top:766px">The standard chunk of Lorem Ipsum used since the 1500s is reproduced below for those interested. Sections 1.10.32 and 1.10.33 from "de Finibus Bonorum et Malorum" by Corvinus are also reproduced in their exact original form, accompanied by English versions.</p>
    <div class="dash" style="top:824px"></div>

    <svg class="post-icon" style="top:853px" width="28" height="24" viewBox="0 0 28 24"><ellipse cx="11" cy="9" rx="11" ry="8" fill="#333"/><path d="M4 14l-2 6 7-4z" fill="#333"/><ellipse cx="19" cy="15" rx="9" ry="6.5" fill="#555"/><path d="M24 19l3 4-7-3z" fill="#555"/></svg>
    <p class="post-meta" style="top:859px"><i>Posted by : Martin</i> Posted on : <i>Dec 22, 2011 5.16 pm</i></p>
    <p class="post-text" style="top:887px">The standard chunk of Lorem Ipsum used since the 1500s is reproduced below for those interested. Sections 1.10.32 and 1.10.33 from "de Finibus Bonorum et Malorum" by Corvinus are also reproduced in their exact original form, accompanied by English versions.</p>
    <div class="dash" style="top:944px"></div>
  </section>

  <section class="featured">
    <h2 class="section-title" style="left:497px">Featured Projects</h2>
    <div class="feat-thumb" style="top:728px"><div role="img" aria-label="Colourful figures standing on an open book" style="background:linear-gradient(#fafafa 40%,#9a9a9a)"></div></div>
    <p class="feat-text" style="top:733px">Sections 1.10.32 and 1.10.33 from "de Finibus Bonorum et Malorum" by Corvinus are also reproduced in their exact original form, accompanied by English versions from the 1914 translation by H. Ashcombe.</p>
    <div class="feat-thumb" style="top:809px"><div role="img" aria-label="Ring of figures holding hands" style="background:radial-gradient(circle,#f6f6f6 25%,#7a7a7a 60%,#f2f2f2)"></div></div>
    <p class="feat-text" style="top:814px">Sections 1.10.32 and 1.10.33 from "de Finibus Bonorum et Malorum" by Corvinus are also reproduced in their exact original form, accompanied by English versions from the 1914 translation by H. Ashcombe.</p>
    <div class="feat-thumb" style="top:890px"><div role="img" aria-label="Team meeting around a table seen from above" style="background:linear-gradient(135deg,#7a3a22,#b26a3a 50%,#3a3a44)"></div></div>
    <p class="feat-text" style="top:895px">Sections 1.10.32 and 1.10.33 from "de Finibus Bonorum et Malorum" by Corvinus are also reproduced in their exact original form, accompanied by English versions from the 1914 translation by H. Ashcombe.</p>
  </section>

  <section class="linkboxes">
    <div class="linkbox" style="left:72px"><h4>Web Design</h4><ul><li>Lorem Ipusem</li><li>Lorem Ipusem</li><li>Lorem Ipusem</li><li>Lorem Ipusem</li><li>Lorem Ipusem</li></ul></div>
    <div class="linkbox" style="left:262px"><h4>Mobile Apps</h4><ul><li>Lorem Ipusem</li><li>Lorem Ipusem</li><li>Lorem Ipusem</li><li>Lorem Ipusem</li><li>Lorem Ipusem</li></ul></div>
    <div class="linkbox" style="left:452px"><h4>Accessible PDF / HTML</h4><ul><li>Lorem Ipusem</li><li>Lorem Ipusem</li><li>Lorem Ipusem</li><li>Lorem Ipusem</li><li>Lorem Ipusem</li></ul></div>
    <div class="linkbox" style="left:642px"><h4>CMS : Quilla / Fernly</h4><ul><li>Lorem Ipusem</li><li>Lorem Ipusem</li><li>Lorem Ipusem</li><li>Lorem Ipusem</li><li>Lorem Ipusem</li></ul></div>
  </section>
</main>

<footer class="footer">
  <span class="accent">Sitemap</span>|<span>Home</span>|<span>Web Design</span>|<span>Mobile Apps</span>|<span>Accessible PDF / HTML</span>|<span>CMS : Quilla / Fernly</span>
</footer>

</body>
</html>
```